Harbor Key Realty - New Agent Opportunity Overview

We want to create a one (1) page brochure to highlight what Harbor Key Realty (a real estate brokerage) offers new agents. I have uploaded a Word doc that has all the text we want on the flyer. We want a professional looking design.
Industry/Entity Type
Real Estate Agent
Colors
3176b5
33a6d7

```html
<!DOCTYPE html>
<html lang="en">
<head>
<meta charset="utf-8">
<title>Harbor Key Realty – New Agent Opportunity</title>
<link href="https://fonts.googleapis.com/css2?family=Barlow+Condensed:wght@500;600;700&family=Barlow:wght@500;600&display=swap" rel="stylesheet">
<style>
  :root{
    --navy:#1b2466;
    --blue:#3158c2;
    --orange:#f3931f;
    --ink:#1d1d2b;
    --paper:#ffffff;
    --bg:#b4b4b4;
    --row:#e3e3e6;
    --row-alt:#f2f2f4;
  }
  *{margin:0;padding:0;box-sizing:border-box}
  html,body{width:1200px;height:900px;overflow:hidden;background:var(--bg)}
  .flyer{position:absolute;left:300px;top:26px;width:600px;height:848px;background:var(--paper);overflow:hidden;font-family:"Barlow Condensed",sans-serif;color:var(--ink)}
  .shapes{position:absolute;inset:0}
  .abs{position:absolute}

  .brand{left:0;right:0;top:34px;display:flex;justify-content:center;align-items:center;gap:12px}
  .brand-mark{width:18px;height:18px;background:var(--navy)}
  .brand-name{font-family:"Barlow",sans-serif;font-weight:600;font-size:26px;letter-spacing:4px;color:var(--navy)}

  .now-open{left:420px;top:78px;width:128px;height:86px;background:var(--orange);color:var(--navy);font-weight:700;font-size:38px;line-height:36px;text-align:center;padding-top:8px}
  .headline{left:40px;top:180px;color:#fff;font-weight:700;font-size:44px;line-height:46px;letter-spacing:.5px;white-space:nowrap}

  .photo{left:300px;top:290px;width:300px;height:180px;clip-path:polygon(0 25px,100% 0,100% 100%,0 100%);background:linear-gradient(135deg,#f4f6f8,#dfe5ea 55%,#c9b8a2)}

  .ignite{left:40px;top:352px;color:var(--navy);font-weight:700;font-size:42px;line-height:40px}
  .ignite small{font-size:27px}

  .support{left:22px;top:486px;width:270px;height:362px;background:var(--orange);border-top-right-radius:56px;padding:20px 16px 0 24px}
  .support h2{font-size:26px;line-height:25px;color:var(--navy);font-weight:700;border-bottom:3px solid var(--navy);padding-bottom:6px;margin-bottom:10px;width:190px}
  .checks{list-style:none}
  .support .checks li{display:flex;gap:7px;font-size:15px;line-height:16px;margin-bottom:5px;font-weight:600}
  .tick{flex:none;width:13px;height:13px;margin-top:2px}
  .edge{left:0;top:770px;width:22px;height:78px;background:var(--blue)}

  .banner{height:28px;background:var(--orange);color:var(--navy);font-weight:700;font-size:20px;line-height:28px;padding-left:12px;white-space:nowrap;clip-path:polygon(0 0,100% 0,94% 100%,0 100%)}
  .direct{left:298px;top:470px;width:294px}
  .leads{left:304px;top:504px;width:290px;display:grid;grid-template-columns:1fr 1.3fr;column-gap:8px;font-size:13px;line-height:16px;font-weight:500}
  .leads ul{list-style:none}
  .leads li{white-space:nowrap}
  .leads li::before{content:"» ";color:var(--navy);font-weight:700}
  .leads li.cont::before{content:"";}

  .comp{left:298px;top:590px;width:294px}
  .comp-list{left:304px;top:624px;width:288px}
  .comp-list .checks li{display:flex;gap:6px;font-size:13px;line-height:15px;margin-bottom:3px;font-weight:500}
  .comp-list .tick{width:11px;height:11px;margin-top:2px}

  .split{left:304px;top:698px;width:284px;border-collapse:collapse;font-size:13px;font-weight:500}
  .split th{background:var(--orange);color:var(--navy);font-size:14px;font-weight:700;text-align:left;padding:3px 8px;white-space:nowrap}
  .split td{padding:1px 8px;line-height:16px;background:var(--row);white-space:nowrap}
  .split tr:nth-child(odd) td{background:var(--row-alt)}
  .split td+td,.split th+th{border-left:2px solid #fff}

  .join{left:330px;top:778px;width:240px;height:24px;background:var(--orange);border-radius:12px;color:var(--navy);font-weight:700;font-size:16px;line-height:24px;text-align:center}
  .contact{left:304px;top:808px;width:292px;display:flex;align-items:center;gap:8px;color:#fff;white-space:nowrap}
  .phone{display:flex;align-items:center;gap:5px;font-weight:700;font-size:24px;line-height:30px}
  .web{font-size:11px;line-height:14px;border-left:1px solid #fff;padding-left:7px;font-weight:500}
</style>
</head>
<body>
<main class="flyer">
  <svg class="shapes" width="600" height="848" viewBox="0 0 600 848">
    <polygon points="0,160 600,96 600,290 0,340" fill="var(--navy)"/>
    <polygon points="510,106 600,96 600,290 510,298" fill="var(--blue)"/>
    <polygon points="300,315 306,470 288,470" fill="var(--navy)"/>
    <rect x="292" y="790" width="308" height="58" fill="var(--navy)"/>
  </svg>

  <div class="abs brand"><span class="brand-mark"></span><span class="brand-name">HARBOR KEY REALTY</span></div>
  <div class="abs now-open">NOW<br>OPEN!</div>
  <h1 class="abs headline">HKR HOME CENTER<br>GAITHERSBURG, MARYLAND</h1>

  <div class="abs photo" role="img" aria-label="Photo of an agent showing a bright new home to a smiling couple"></div>

  <p class="abs ignite">IGNITE <small>YOUR</small><br>REAL ESTATE<br>BUSINESS</p>

  <section class="abs support">
    <h2>COMPLETE<br>SUPPORT SYSTEM</h2>
    <ul class="checks">
      <li><svg class="tick" viewBox="0 0 14 14"><circle cx="7" cy="7" r="7" fill="var(--ink)"/><path d="M3.5 7.2l2.3 2.3 4.7-4.7" stroke="#fff" stroke-width="1.8" fill="none"/></svg>Powerful Suite of Cloud Based Tools</li>
      <li><svg class="tick" viewBox="0 0 14 14"><circle cx="7" cy="7" r="7" fill="var(--ink)"/><path d="M3.5 7.2l2.3 2.3 4.7-4.7" stroke="#fff" stroke-width="1.8" fill="none"/></svg>IDX, CRM and Transaction Management</li>
      <li><svg class="tick" viewBox="0 0 14 14"><circle cx="7" cy="7" r="7" fill="var(--ink)"/><path d="M3.5 7.2l2.3 2.3 4.7-4.7" stroke="#fff" stroke-width="1.8" fill="none"/></svg>HKR Call Center Support for Leads and Deals</li>
      <li><svg class="tick" viewBox="0 0 14 14"><circle cx="7" cy="7" r="7" fill="var(--ink)"/><path d="M3.5 7.2l2.3 2.3 4.7-4.7" stroke="#fff" stroke-width="1.8" fill="none"/></svg>Transaction Coordinator</li>
      <li><svg class="tick" viewBox="0 0 14 14"><circle cx="7" cy="7" r="7" fill="var(--ink)"/><path d="M3.5 7.2l2.3 2.3 4.7-4.7" stroke="#fff" stroke-width="1.8" fill="none"/></svg>Virtual Assistants Available</li>
      <li><svg class="tick" viewBox="0 0 14 14"><circle cx="7" cy="7" r="7" fill="var(--ink)"/><path d="M3.5 7.2l2.3 2.3 4.7-4.7" stroke="#fff" stroke-width="1.8" fill="none"/></svg>24/7 Workspace Access</li>
      <li><svg class="tick" viewBox="0 0 14 14"><circle cx="7" cy="7" r="7" fill="var(--ink)"/><path d="M3.5 7.2l2.3 2.3 4.7-4.7" stroke="#fff" stroke-width="1.8" fill="none"/></svg>Coaching / Mentoring</li>
      <li><svg class="tick" viewBox="0 0 14 14"><circle cx="7" cy="7" r="7" fill="var(--ink)"/><path d="M3.5 7.2l2.3 2.3 4.7-4.7" stroke="#fff" stroke-width="1.8" fill="none"/></svg>Social Media / Marketing Expertise</li>
      <li><svg class="tick" viewBox="0 0 14 14"><circle cx="7" cy="7" r="7" fill="var(--ink)"/><path d="M3.5 7.2l2.3 2.3 4.7-4.7" stroke="#fff" stroke-width="1.8" fill="none"/></svg>Nationwide Partnerships with Top Lenders</li>
    </ul>
  </section>
  <div class="abs edge"></div>

  <h2 class="abs banner direct">CONSUMER DIRECT ADVANTAGE</h2>
  <div class="abs leads">
    <ul>
      <li>Lender Referrals</li>
      <li>Nestfinder Leads</li>
      <li>Shared Lender Leads</li>
      <li>HomeSeek.net /</li>
      <li class="cont">OpenDoorwayList.com</li>
    </ul>
    <ul>
      <li>Credit Trigger Campaigns</li>
      <li>Consumer Behavior Campaigns</li>
      <li>HKR Call Center Marketing Team</li>
      <li>HKR Sponsored Local Events</li>
    </ul>
  </div>

  <h2 class="abs banner comp">MAXIMIZED COMPENSATION</h2>
  <div class="abs comp-list">
    <ul class="checks">
      <li><svg class="tick" viewBox="0 0 14 14"><circle cx="7" cy="7" r="7" fill="var(--navy)"/><path d="M3.5 7.2l2.3 2.3 4.7-4.7" stroke="#fff" stroke-width="1.8" fill="none"/></svg>No desk fees. No royalty fees. No franchise fees.</li>
      <li><svg class="tick" viewBox="0 0 14 14"><circle cx="7" cy="7" r="7" fill="var(--navy)"/><path d="M3.5 7.2l2.3 2.3 4.7-4.7" stroke="#fff" stroke-width="1.8" fill="none"/></svg>Company paid E&amp;O</li>
      <li><svg class="tick" viewBox="0 0 14 14"><circle cx="7" cy="7" r="7" fill="var(--navy)"/><path d="M3.5 7.2l2.3 2.3 4.7-4.7" stroke="#fff" stroke-width="1.8" fill="none"/></svg>Transaction fee of $550 includes Transaction Coordinator</li>
    </ul>
  </div>
  <table class="abs split">
    <tr><th>TYPE OF DEAL</th><th>COMMISSION SPLIT</th></tr>
    <tr><td>Self-Generated</td><td>90% / 10%</td></tr>
    <tr><td>Lender Referred Leads</td><td>70% / 30%</td></tr>
    <tr><td>HKR Generated Leads / Referrals</td><td>55% / 45%</td></tr>
  </table>

  <div class="abs join">JOIN HARBOR KEY REALTY</div>
  <div class="abs contact">
    <span class="phone"><svg width="16" height="16" viewBox="0 0 24 24"><path d="M6.6 10.8a15 15 0 006.6 6.6l2.2-2.2a1 1 0 011-.25 11.4 11.4 0 003.6.57 1 1 0 011 1V20a1 1 0 01-1 1A17 17 0 013 4a1 1 0 011-1h3.5a1 1 0 011 1c0 1.250.2 2.450.57 3.57a1 1 0 01-.25 1z" fill="var(--blue)"/></svg>555 014 2280</span>
    <span class="web">hello@harborkeyrealty.com<br>www.harborkeyrealty.com</span>
  </div>
</main>
</body>
</html>
```